Design the Keystone HR business card for my new business

I've just had a logo designed (attached) for my new business doing HR consulting. I'm a one person operation at this stage, my aim is to provide support and help to small to medium sized businesses with their people objectives or issues.

I'm not really into anything overly flashy, I'm not a PR or marketing agency. I'd like my card to look modern, professional and not gimmicky.

I'm thinking black front (to go with logo), double sided with details on the back, maybe in a different colour?

Logo attached in several different formats.

Front of the card to have logo and added text: People and Development Solutions

Back of the card to also feature logo in some way and say:
Megan Tulloch
PO Box (TBA)
Marrowvale QLD 4391
0438 512 976
megan@keystonehr.com.au
www.keystonehr.com.au

Target Market(s)

Small to medium businesses / business owners.

Industry/Entity Type

Marketing

Requirements
Must have
• Double sided business card.
Should not have
• Anything overly gimmicky.

```html
<!DOCTYPE html>
<html lang="en">
<head>
<meta charset="utf-8">
<title>Keystone HR Consulting – Business Card</title>
<link rel="stylesheet" href="https://fonts.googleapis.com/css2?family=Questrial&display=swap">
<style>
  :root {
    --backdrop: #d8cec7;
    --card: #272526;
    --text-light: #e4e4e4;
    --text-soft: #cfcfcf;
    --purple: #7b3fa8;
    --purple-deep: #4f2472;
    --band-grey: #4b4a4c;
  }
  * { margin: 0; padding: 0; box-sizing: border-box; }
  html, body {
    width: 1200px;
    height: 900px;
    overflow: hidden;
    background: var(--backdrop);
    font-family: "Questrial", sans-serif;
  }
  .card-pair {
    position: absolute;
    left: 223px;
    top: 135px;
    display: flex;
    gap: 34px;
  }
  .card {
    position: relative;
    width: 360px;
    height: 630px;
    background: var(--card);
    overflow: hidden;
    color: var(--text-light);
  }
  .brand-dot {
    position: absolute;
    border-radius: 50%;
    border: 2px solid var(--purple);
  }
  .brand-name {
    position: absolute;
    color: var(--text-light);
    font-weight: 400;
    line-height: 1;
    white-space: nowrap;
  }
  .brand-name span { display: block; }

  /* back: contact side */
  .card--back .brand-dot { left: 36px; top: 68px; width: 108px; height: 108px; }
  .card--back .brand-name { left: 160px; top: 92px; }
  .card--back .brand-word { font-size: 36px; letter-spacing: -0.5px; }
  .card--back .brand-sub { font-size: 19px; margin-top: 4px; }

  .contact-name {
    position: absolute;
    left: 48px;
    top: 404px;
    font-size: 22px;
    letter-spacing: 1px;
    color: #ffffff;
  }
  .contact-details {
    position: absolute;
    left: 48px;
    top: 456px;
    list-style: none;
    font-size: 14.5px;
    line-height: 21.6px;
    color: var(--text-soft);
  }
  .contact-details b { color: #ffffff; font-weight: 400; }

  /* front: brand side */
  .card--front .brand-dot { left: 97px; top: 98px; width: 164px; height: 164px; }
  .card--front .brand-name { left: 0; right: 0; top: 282px; text-align: center; }
  .card--front .brand-word { font-size: 58px; letter-spacing: -1px; }
  .card--front .brand-sub { font-size: 29px; margin-top: 8px; padding-left: 30px; }

  .tagline {
    position: absolute;
    left: 0;
    right: 0;
    top: 433px;
    text-align: center;
    font-size: 16px;
    color: var(--text-soft);
  }

  .swoosh {
    position: absolute;
    left: 0;
    bottom: 0;
    width: 360px;
    height: 90px;
  }
</style>
</head>
<body>
  <svg width="0" height="0" style="position:absolute">
    <defs>
      <linearGradient id="swoosh-purple" x1="0" x2="1" y1="0" y2="0">
        <stop offset="0" stop-color="#7b3fa8"/>
        <stop offset="0.55" stop-color="#6a3296"/>
        <stop offset="1" stop-color="#4f2472"/>
      </linearGradient>
    </defs>
  </svg>

  <main class="card-pair">
    <section class="card card--back" aria-label="Card back with contact details">
      <div class="brand-dot"></div>
      <div class="brand-name">
        <span class="brand-word">Keystone</span>
        <span class="brand-sub">HR Consulting</span>
      </div>

      <h1 class="contact-name">Megan Tulloch</h1>
      <ul class="contact-details">
        <li>PO Box (TBA)</li>
        <li>Marrowvale QLD 4391</li>
        <li><b>P</b> : 0438 512 976</li>
        <li><b>E</b> : megan@keystonehr.com.au</li>
        <li>www.keystonehr.com.au</li>
      </ul>

      <svg class="swoosh" viewBox="0 0 360 90" preserveAspectRatio="none" aria-hidden="true">
        <path d="M0,26 C110,40 240,22 360,0 L360,90 L0,90 Z" fill="var(--band-grey)"/>
        <path d="M0,36 C110,52 240,34 360,12 L360,90 L0,90 Z" fill="url(#swoosh-purple)"/>
      </svg>
    </section>

    <section class="card card--front" aria-label="Card front with brand">
      <div class="brand-dot"></div>
      <div class="brand-name">
        <span class="brand-word">Keystone</span>
        <span class="brand-sub">HR Consulting</span>
      </div>

      <p class="tagline">People and Development Solutions</p>

      <svg class="swoosh" viewBox="0 0 360 90" preserveAspectRatio="none" aria-hidden="true">
        <path d="M0,26 C110,40 240,22 360,0 L360,90 L0,90 Z" fill="var(--band-grey)"/>
        <path d="M0,36 C110,52 240,34 360,12 L360,90 L0,90 Z" fill="url(#swoosh-purple)"/>
      </svg>
    </section>
  </main>
</body>
</html>
```